KT Crewing business card

Require business card which includes:
Company name: KT CREWING PTY LTD
Email: Mick@ktcrewing.com.au
Phone: 0431 556 208
ACN: 517 238 649

slogan: Onsite Auto Electrician Labour hire

Details and logo on top side
Logo only on bottom side

colour codes : #F15A29 , #939598

Target Market(s)

Western Australia mining sector

Industry/Entity Type

Mining

Contact Information for Business Card

Require business card which includes: Company name: KT CREWING PTY LTD Email: Mick@ktcrewing.com.au Phone: 0431 556 208 ACN: 517 238 649 slogan: Onsite Auto Electrician Labour hire Details and logo on top side Logo only on bottom side colour codes : #F15A29 , #939598

Colors
EE7325
F08F49
F5BC92
FAE3D3
FDF4ED

Requirements
Must have
• double sided

```html
<!DOCTYPE html>
<html lang="en">
<head>
<meta charset="UTF-8">
<title>KT Crewing Business Card</title>
<link rel="stylesheet" href="https://fonts.googleapis.com/css2?family=Exo+2:wght@400;600;800&display=swap">
<style>
  :root {
    --bg: #0c0c0d;
    --card: #2a2a2c;
    --card-back: #252527;
    --orange: #F15A29;
    --grey: #939598;
    --ink: #111111;
    --emboss: #3c3c3f;
  }
  * { margin: 0; padding: 0; box-sizing: border-box; }
  html, body { width: 1200px; height: 820px; overflow: hidden; }
  body {
    background: var(--bg);
    font-family: "Exo 2", sans-serif;
    position: relative;
  }
  .card {
    position: absolute;
    top: 262px;
    width: 520px;
    height: 297px;
    overflow: hidden;
  }
  .card-front {
    left: 50px;
    background: var(--card);
    border-left: 4px solid var(--orange);
  }
  .card-back {
    left: 630px;
    background: var(--card-back);
    border-bottom: 5px solid var(--orange);
    display: flex;
    align-items: center;
    justify-content: center;
  }
  .brand {
    font-weight: 800;
    color: var(--orange);
    line-height: 1;
    display: flex;
    align-items: center;
    gap: 10px;
  }
  .brand-front { position: absolute; top: 44px; right: 40px; font-size: 40px; }
  .brand-mark { width: 14px; height: 14px; background: var(--grey); }
  .brand-back { font-size: 58px; color: var(--emboss); }
  .divider {
    position: absolute;
    left: 30px; right: 30px; top: 165px;
    height: 1px;
    background: var(--orange);
  }
  .person { position: absolute; left: 30px; top: 116px; }
  .person-name {
    font-weight: 800;
    font-size: 22px;
    color: var(--orange);
    letter-spacing: 0.5px;
    line-height: 1;
  }
  .person-title { font-size: 14px; color: var(--grey); margin-top: 3px; }
  .contacts {
    position: absolute; left: 30px; top: 178px;
    list-style: none;
    font-size: 14px; color: var(--grey);
  }
  .contacts li { display: flex; align-items: center; gap: 8px; line-height: 22px; }
  .contacts svg { width: 14px; height: 14px; fill: none; stroke: var(--orange); stroke-width: 2; }
  .acn {
    position: absolute; right: 30px; top: 184px;
    font-size: 13px; color: var(--grey);
  }
  .acn-label { color: var(--orange); }
  .slogan-band {
    position: absolute; left: 0; right: 0; bottom: 0;
    height: 52px;
    background: var(--orange);
    display: flex; align-items: center; justify-content: center;
  }
  .slogan { font-weight: 800; font-size: 21px; color: var(--ink); }
</style>
</head>
<body>
  <section class="card card-front" aria-label="Business card front">
    <div class="brand brand-front"><span class="brand-mark"></span>KT Crewing</div>
    <div class="person">
      <p class="person-name">MARCUS HALE</p>
      <p class="person-title">Managing Director</p>
    </div>
    <div class="divider"></div>
    <ul class="contacts">
      <li>
        <svg viewBox="0 0 24 24" aria-hidden="true"><path d="M5 3h4l2 5-2.5 1.5a11 11 0 0 0 6 6L16 13l5 2v4a2 2 0 0 1-2 2A16 16 0 0 1 3 5a2 2 0 0 1 2-2z"/></svg>
        0431 556 208
      </li>
      <li>
        <svg viewBox="0 0 24 24" aria-hidden="true"><rect x="2" y="5" width="20" height="14"/><path d="M2 5l10 8 10-8"/></svg>
        Mick@ktcrewing.com.au
      </li>
    </ul>
    <p class="acn"><span class="acn-label">ACN:</span> 517 238 649</p>
    <div class="slogan-band"><p class="slogan">Onsite Auto Electrician Labour hire</p></div>
  </section>

  <section class="card card-back" aria-label="Business card back">
    <div class="brand brand-back">KT Crewing</div>
  </section>
</body>
</html>
```